Corrindale Planners, LLC Stationary

Corrindale Planners, LLC is a new financial planning and consulting company. We are looking for designs on business cards, letterhead, envelopes, and anything else that would be useful. Our preference for business card design is two sided. We are looking for a professional and clean look with incorporating the logo and patriotic feel. Thank you to all who participate and good luck!

```html
<!DOCTYPE html>
<html lang="en">
<head>
<meta charset="utf-8">
<title>Corrindale Planners, LLC – Business Card</title>
<link rel="stylesheet" href="https://fonts.googleapis.com/css2?family=Michroma&family=Montserrat:wght@400;600&display=swap">
<style>
  :root {
    --page-bg: #2b2b2b;
    --card-blue: #2f5676;
    --card-blue-light: #3d6a8c;
    --card-white: #ffffff;
    --navy: #1f3d63;
    --red: #c8353a;
    --ink: #4a4f58;
    --rule: #c9ccd1;
  }
  * { margin: 0; padding: 0; box-sizing: border-box; }
  html, body {
    width: 1200px; height: 676px; overflow: hidden;
    background: var(--page-bg);
  }
  .canvas {
    position: relative; width: 1200px; height: 676px;
    display: flex; align-items: center; justify-content: center; gap: 48px;
  }
  .card {
    width: 500px; height: 286px; position: relative;
    border-radius: 3px;
    box-shadow: 0 14px 30px rgba(0,0,0,.45);
  }
  .card-back {
    background: linear-gradient(135deg, var(--card-blue-light), var(--card-blue));
  }
  .card-back .brand-name {
    position: absolute; left: 44px; top: 58px;
    color: var(--card-white);
    font: 400 19px/1 "Michroma", sans-serif;
    letter-spacing: 1px;
    display: flex; align-items: center; gap: 10px;
  }
  .brand-dot {
    width: 14px; height: 14px; border-radius: 50%;
    background: var(--red);
  }
  .card-front { background: var(--card-white); }
  .card-front .brand-name {
    position: absolute; right: 34px; top: 46px;
    color: var(--navy);
    font: 400 17px/1 "Michroma", sans-serif;
    letter-spacing: .5px;
    display: flex; align-items: center; gap: 9px;
  }
  .person {
    position: absolute; left: 34px; top: 126px;
    font-family: "Montserrat", sans-serif;
  }
  .person-name {
    color: var(--navy); font-size: 14px; font-weight: 600;
    letter-spacing: 1px; text-transform: uppercase;
  }
  .person-title {
    color: var(--red); font-size: 10px; letter-spacing: 1px;
    text-transform: uppercase; margin-top: 3px;
  }
  .contact {
    position: absolute; left: 34px; right: 34px; top: 200px;
    font: 400 10px/1.6 "Montserrat", sans-serif;
    color: var(--ink);
  }
  .contact .label { color: var(--red); font-weight: 600; }
  .contact .sep { color: var(--rule); margin: 0 4px; }
  .contact-rule {
    position: absolute; left: 34px; right: 34px; top: 248px;
    height: 1px; background: var(--rule);
  }
</style>
</head>
<body>
<main class="canvas">
  <section class="card card-back" aria-label="Business card, reverse side">
    <div class="brand-name"><span class="brand-dot"></span>Corrindale Planners, LLC</div>
  </section>

  <section class="card card-front" aria-label="Business card, front side">
    <div class="brand-name"><span class="brand-dot"></span>Corrindale Planners, LLC</div>
    <div class="person">
      <p class="person-name">Daniel Whitmore</p>
      <p class="person-title">Managing Director</p>
    </div>
    <div class="contact">
      <p>Level 12, Harbourline House, 18 Keel Street, Marlow NW 2041<span class="sep">|</span><span class="label">t:</span> 1300 552 718</p>
      <p><span class="label">f:</span> 1800 413 2270<span class="sep">|</span><span class="label">e:</span> daniel@corrindale.com<span class="sep">|</span><span class="label">w:</span> www.corrindale.com</p>
    </div>
    <div class="contact-rule"></div>
  </section>
</main>
</body>
</html>
```